Oil and gas industry project solutions company needs professional cards with Canadian aboriginal fee

We are a aboriginally owned company that is focused on Project Planning, Management, Inspection & Consulting for Canada's Petroleum Industry. We have a logo that we would like to incorporate into a professional looking business card. We are professionals that offer services from project inception to completion.

Target Market(s)

Major industry leaders like NorvaLine, Brisk, Vorkantrel, Pelquist etc.

Industry/Entity Type

Industry

Contact Information for Business Card

Milo Rensford
milo@orvelpike.ca
250 555 0187

Requirements
Must have
• OrvelPike Inc. logo.
• Address is: RR4, Site2, Comp17 Fort St. John, BC V9X 2K3 Traditional Territory of the Treaty 8 People
• Colors that are in logo
• Banner or picture on back
• Ability to put different names and contacts
• Website: orvelpike.ca
• "Project Planning, Management, Inspection & Consulting for Canada's Petroleum Industry"

```html
<!DOCTYPE html>
<html lang="en">
<head>
<meta charset="utf-8">
<title>OrvelPike Inc. Business Cards</title>
<link rel="stylesheet" href="https://fonts.googleapis.com/css2?family=Didact+Gothic&family=Exo+2:wght@500;600&display=swap">
<style>
  :root {
    --navy: #2b3475;
    --navy-deep: #1f2760;
    --green: #6cbf3a;
    --lavender: #dfe2f2;
    --lavender-light: #eceef8;
    --steel: #5e6f96;
    --sky: #9fb3d6;
    --amber: #d7a92a;
    --ink: #2b3475;
    --page: #f2f2f0;
  }
  * { box-sizing: border-box; margin: 0; padding: 0; }
  html, body { width: 1200px; height: 789px; overflow: hidden; }
  body {
    background: var(--page);
    font-family: "Didact Gothic", "Century Gothic", sans-serif;
    color: var(--ink);
    position: relative;
  }
  .card {
    position: absolute;
    left: 280px;
    width: 640px;
    height: 366px;
    background: var(--lavender);
    overflow: hidden;
    box-shadow: 0 4px 14px rgba(0,0,0,0.18);
  }
  .card--front { top: 18px; }
  .card--back { top: 405px; }

  .photo { position: absolute; }
  .front-photo-top {
    left: 0; top: 0; width: 100%; height: 150px;
    background: linear-gradient(90deg, var(--navy-deep) 0%, var(--steel) 28%, var(--sky) 50%, #8a6f4a 72%, var(--amber) 100%);
  }
  .front-fade {
    position: absolute; left: 0; top: 60px; width: 100%; height: 100px;
    background: linear-gradient(180deg, rgba(223,226,242,0) 0%, var(--lavender) 80%);
  }
  .front-band {
    position: absolute; left: 0; top: 214px; width: 100%; height: 58px;
    background: var(--navy);
  }
  .tagline {
    position: absolute; left: 0; top: 222px; width: 100%;
    text-align: center; color: #fff; font-size: 17px; line-height: 22px;
    font-style: italic; letter-spacing: 0.3px;
  }
  .front-photo-bottom {
    left: 0; top: 272px; width: 100%; height: 94px;
    background: linear-gradient(90deg, var(--steel) 0%, var(--amber) 30%, #4a5677 55%, var(--navy-deep) 100%);
  }

  .brand {
    position: absolute; display: flex; align-items: center; gap: 14px;
  }
  .brand__mark {
    width: 44px; height: 44px; border-radius: 50%; background: var(--green); flex: none;
  }
  .brand__name {
    font-family: "Didact Gothic", "Century Gothic", sans-serif;
    color: var(--navy); font-size: 44px; line-height: 1; letter-spacing: 0.5px;
  }
  .card--front .brand { left: 120px; top: 142px; }
  .card--back .brand { left: 40px; top: 100px; }
  .card--back .brand__name { font-size: 38px; }

  .divider {
    position: absolute; left: 396px; top: 18px; width: 1px; height: 200px; background: var(--navy);
  }
  .person {
    position: absolute; left: 416px; top: 30px; display: flex; align-items: center; gap: 10px;
  }
  .person__icon { width: 30px; height: 30px; }
  .person__name {
    font-family: "Exo 2", sans-serif; font-weight: 600; font-size: 21px; color: var(--navy);
  }
  .contacts {
    position: absolute; left: 420px; top: 112px; list-style: none;
    font-size: 14px; line-height: 19px; color: var(--navy);
  }
  .contacts li { display: flex; gap: 9px; align-items: flex-start; margin-bottom: 4px; }
  .contacts svg { width: 14px; height: 14px; flex: none; margin-top: 3px; }

  .back-band {
    position: absolute; left: 0; top: 232px; width: 100%; height: 46px; background: var(--navy);
  }
  .website {
    position: absolute; right: 30px; top: 238px; color: #fff; font-size: 26px; line-height: 34px;
    letter-spacing: 0.5px;
  }
  .back-photo-bottom {
    left: 0; top: 278px; width: 100%; height: 88px;
    background: linear-gradient(90deg, var(--lavender-light) 0%, var(--lavender-light) 22%, var(--amber) 38%, #4a5677 60%, var(--steel) 80%, var(--navy-deep) 100%);
  }
</style>
</head>
<body>

<section class="card card--front" aria-label="Card front">
  <div class="photo front-photo-top" role="img" aria-label="Collage of pipeline field work: crew in high-visibility gear in snow and coated pipe sections"></div>
  <div class="front-fade"></div>
  <div class="brand">
    <span class="brand__mark"></span>
    <span class="brand__name">OrvelPike Inc.</span>
  </div>
  <div class="front-band"></div>
  <p class="tagline">"Project Planning, Management, Inspection &amp; Consulting<br>for Canada's Petroleum Industry"</p>
  <div class="photo front-photo-bottom" role="img" aria-label="Yellow pipelayer machinery and a plant structure at a petroleum site"></div>
</section>

<section class="card card--back" aria-label="Card back">
  <div class="brand">
    <span class="brand__mark"></span>
    <span class="brand__name">OrvelPike Inc.</span>
  </div>
  <div class="divider"></div>
  <div class="person">
    <svg class="person__icon" viewBox="0 0 30 30" aria-hidden="true">
      <circle cx="15" cy="15" r="15" fill="var(--green)"/>
      <circle cx="15" cy="15" r="11" fill="none" stroke="#fff" stroke-width="1.5"/>
      <circle cx="15" cy="11.5" r="3.3" fill="#fff"/>
      <path d="M9 21.5c0-3.6 2.7-5.6 6-5.6s6 2 6 5.6z" fill="#fff"/>
    </svg>
    <span class="person__name">Milo Rensford</span>
  </div>
  <ul class="contacts">
    <li>
      <svg viewBox="0 0 14 14" aria-hidden="true"><circle cx="7" cy="7" r="7" fill="var(--green)"/><path d="M4.3 3.6l1.4-.3.8 1.8-.9.7a5 5 0 0 0 2.6 2.6l.7-.9 1.8.8-.3 1.4c-3.4.2-6.3-2.7-6.1-6.1z" fill="#fff"/></svg>
      <span>250 555 0187</span>
    </li>
    <li>
      <svg viewBox="0 0 14 14" aria-hidden="true"><rect x="1" y="3" width="12" height="8" rx="1" fill="var(--green)"/><path d="M1.5 3.5L7 7.8l5.5-4.3" fill="none" stroke="#fff" stroke-width="1.1"/></svg>
      <span>milo@orvelpike.ca</span>
    </li>
    <li>
      <svg viewBox="0 0 14 14" aria-hidden="true"><path d="M7 13.5S2.2 8.4 2.2 5.3a4.8 4.8 0 0 1 9.6 0C11.8 8.4 7 13.5 7 13.5z" fill="var(--green)"/><circle cx="7" cy="5.3" r="1.7" fill="#fff"/></svg>
      <span>RR4, Site2, Comp17 Fort St. John,<br>BC V9X 2K3</span>
    </li>
  </ul>
  <div class="back-band"></div>
  <p class="website">orvelpike.ca</p>
  <div class="photo back-photo-bottom" role="img" aria-label="Strip of pipeline site imagery: yellow machinery, plant structure and coated pipe"></div>
</section>

</body>
</html>
```